International freight forwarder experienced in perishable handling needs a web design

We need a website designed that will allow us to capture more customers through the website. We would like a visually appealing design that is not so heavy on text. Our business covers the logistics and freight forwarding industries and we have offices in South America and the USA. Our main customers are importers USA, Europe, Asia and Russia and we currently work almost exclusively with perishable products such as fresh cut flowers, fresh exotics fruits, cacao, fresh fish etc. We would like to convey a fresh, modern approach to freight forwarding focusing on concepts such as - time sensitive, anytime-anywhere delivery, innovation, experience, reliability and confidence. Should include links with Chatterpost and Workvine. Our core solutions include: Core Services
*Air Freight
*Ocean Freight
*Warehousing & Distribution
Our industry solutions cover
*Flowers
*FMCG including, fruits, vegetables
*Live animals
*Automotive
*Consumer Goods
*Industrial
*Oil & Gas
*Pharma
* Event logistics
* Project logistics

Target Market(s)

Importers in Europe, USA, Asia, Middle East and Russia

Number of Pages Required

4 page

Font styles to use
Sans Serif

Colors
a1cd39
606060
000000

Requirements
Must have
• Photos of fresh cut flowers, FMCG such as cacao, fresh fish (packaged for shipping), fresh exotic fruits, pharma products (packaged for shipping), oil and gas etc. Internal customer login access
Nice to have
• Photos of cargo shipping carriers and cargo airline carriers. Features similar to those of following website http://www.vantoshipping.example/eng/main/index.jsp?FromURL=web
Should not have
• Too much text, needs to be visually pleasing

```html
<!DOCTYPE html>
<html lang="en">
<head>
<meta charset="utf-8">
<title>Corvana Freight</title>
<link href="https://fonts.googleapis.com/css2?family=Arimo:wght@400;700&display=swap" rel="stylesheet">
<style>
:root{
  --green:#8cbf2d;
  --green-light:#a1cd39;
  --grey:#606060;
  --dark:#3a3a3a;
  --ink:#222;
  --muted:#8a8a8a;
  --pale:#efefef;
  --white:#fff;
}
*{box-sizing:border-box;margin:0;padding:0}
html,body{width:761px;height:1200px;overflow:hidden;background:var(--white);font-family:"Arimo",Arial,sans-serif;color:var(--ink)}
.page{position:relative;width:761px;height:1200px}
.abs{position:absolute}

/* header */
.header{left:0;top:0;width:761px;height:60px;background:var(--white);border-bottom:1px solid #ddd}
.brand{left:184px;top:14px;display:flex;align-items:center;gap:5px;font-size:13px;font-weight:700;color:var(--dark)}
.brand .dot{width:13px;height:13px;border-radius:50%;background:var(--green)}
.phone{left:404px;top:9px;display:flex;align-items:center;gap:5px;font-size:9px;color:var(--ink)}
.search{left:492px;top:7px;width:63px;height:15px;background:#bdbdbd;color:#eee;font-size:6px;padding:4px 5px}
.search-btn{left:559px;top:7px;width:16px;height:15px;background:#555}
.nav{left:325px;top:35px;display:flex;height:25px;font-size:7px;color:var(--dark)}
.nav span{padding:6px 7px 0}
.nav .active{background:var(--green);color:var(--white);font-weight:700}

/* hero */
.hero{left:0;top:60px;width:761px;height:206px;background:radial-gradient(circle at 40% 50%,#6a6a6a,#2e2e2e 75%)}
.hero-art{left:108px;top:64px;width:308px;height:200px;background:radial-gradient(ellipse at 50% 55%,rgba(140,191,45,.55),rgba(120,120,120,.35) 60%,rgba(60,60,60,0) 100%)}
.booking{left:418px;top:74px;width:157px;height:175px;background:var(--green)}
.booking-head{background:#333;color:var(--white);padding:8px 6px 6px;text-align:center}
.booking-head h2{font-size:7.5px;font-weight:700;letter-spacing:.2px}
.booking-head p{font-size:4.8px;margin-top:3px;color:#ddd;line-height:1.3}
.field{position:absolute;left:10px;width:139px;height:19px;background:var(--white);font-size:5px;color:#555;padding:7px 5px 0}
.cal{position:absolute;left:140px;top:111px;width:11px;height:11px;border:1.5px solid var(--white);border-radius:1px}
.book-btn{position:absolute;left:10px;top:136px;width:139px;height:24px;background:#333;color:var(--white);font-size:6.5px;font-weight:700;text-align:center;padding-top:9px}
.hero-dots{left:362px;top:266px;width:37px;height:11px;background:#333;border-radius:0 0 3px 3px;display:flex;justify-content:center;gap:3px;padding-top:4px}
.hero-dots i,.dots i{display:block;width:3px;height:3px;border-radius:50%;background:var(--white)}
.hero-dots i.on,.dots i.on{background:var(--green)}

/* section headings */
.sec-head{left:0;width:761px;text-align:center}
.sec-head p{font-size:6.5px;color:#444}
.sec-head h2{display:inline-block;font-size:10px;font-weight:700;color:var(--dark);padding:0 6px 2px;border-bottom:1px solid var(--green);margin-top:1px}
.on-dark p{color:#ddd}.on-dark h2{color:var(--white)}

/* services */
.service{width:110px;text-align:center;top:334px}
.service svg{display:block;margin:0 auto}
.service h3{font-size:8px;font-weight:400;margin-top:10px;color:var(--ink)}
.service p{font-size:5.6px;color:var(--muted);line-height:1.35;margin-top:5px}
.more{display:inline-block;margin-top:8px;background:var(--green);color:var(--white);font-size:5.5px;padding:4px 4px;border:1px solid #6a9a1e}

/* products */
.products{left:0;top:472px;width:761px;height:239px;background:var(--pale)}
.tile{width:85px;height:72px}
.tile span{display:block;height:16px;background:var(--green);color:var(--white);font-size:7px;text-align:center;padding-top:4px}
.tile .grey{background:#5a5a5a}
.tile div{height:56px}

/* testimonial */
.testimonial{left:0;top:711px;width:761px;height:188px;background:radial-gradient(ellipse at 50% 60%,#5e5e5e,#333 80%)}
.quote-mark{font-size:26px;color:#aaa;font-weight:700;font-family:Georgia,serif}
.quote-text{left:205px;top:768px;width:350px;text-align:center;color:var(--white);font-size:6px;line-height:1.3}
.author{left:0;top:805px;width:761px;text-align:center;font-size:8px;color:var(--green-light)}
.author small{font-size:6px;color:var(--white)}
.avatar{left:362px;top:822px;width:38px;height:38px;border-radius:50%;border:2px solid var(--white);background:linear-gradient(#b9b9b9,#6d6d6d)}
.dots{left:0;top:875px;width:761px;display:flex;justify-content:center;gap:4px}

/* quote */
.quote-panel{left:209px;top:955px;width:345px;height:93px;background:#3f3f3f;border-radius:3px;box-shadow:0 6px 6px -4px rgba(0,0,0,.3)}
.q-field{width:102px;height:17px;background:var(--white);font-size:5px;color:#555;padding:6px 5px 0;border:1px solid #ccc}
.q-field.select::after{content:"▾";float:right;font-size:5px}
.quote-btn{left:330px;top:1030px;width:101px;height:22px;background:var(--green);color:var(--white);font-size:8px;font-weight:700;text-align:center;padding-top:7px}

/* footer */
.footer{left:0;top:1090px;width:761px;height:90px;background:var(--green);border-top:3px solid #a9d24a}
.foot-brand{left:186px;top:1116px;display:flex;align-items:center;gap:5px;font-size:12px;font-weight:700;color:var(--ink)}
.foot-brand .dot{width:12px;height:12px;border-radius:50%;background:var(--ink)}
.foot-col h4{font-size:6.5px;font-weight:700;color:var(--ink);margin-bottom:8px}
.foot-col p,.foot-col li{font-size:5px;color:#222;line-height:1.6}
.foot-col ul{list-style:none}
.foot-col li::before{content:"■ ";font-size:3px;vertical-align:middle}
.contact-row{display:flex;gap:6px;align-items:flex-start;margin-bottom:4px}
.social{display:grid;grid-template-columns:repeat(3,auto);gap:4px 5px}
.social span{font-size:5px;color:var(--white);background:#3d3d3d;padding:2px 3px}
.foot-divider{left:424px;top:1100px;width:1px;height:72px;background:#b9da6b}
.bottom{left:0;top:1180px;width:761px;height:20px;font-size:5px;color:#333}
.bottom .l{position:absolute;left:186px;top:8px}
.bottom .r{position:absolute;left:495px;top:8px}
</style>
</head>
<body>
<div class="page">

  <header class="abs header"></header>
  <div class="abs brand"><span class="dot"></span>Corvana Freight</div>
  <div class="abs phone">
    <svg width="14" height="14" viewBox="0 0 14 14"><circle cx="7" cy="7" r="6" fill="none" stroke="#222" stroke-width="1.5"/><path d="M4.5 5c.5 2 2 3.6 4 4.3l.9-.9" fill="none" stroke="#222" stroke-width="1.2"/></svg>
    +1-555-014729
  </div>
  <div class="abs search">Search</div>
  <div class="abs search-btn">
    <svg width="16" height="15" viewBox="0 0 16 15"><circle cx="7" cy="6.5" r="3" fill="none" stroke="#fff" stroke-width="1.2"/><path d="M9.2 8.7l2.5 2.5" stroke="#fff" stroke-width="1.3"/></svg>
  </div>
  <nav class="abs nav">
    <span class="active">Home</span><span>About Us</span><span>Services</span><span>Freight Tracking</span><span>Blog</span><span>Contact Us</span>
  </nav>

  <section class="abs hero"></section>
  <div class="abs hero-art" role="img" aria-label="Cargo plane, globe, forklift and freight container truck"></div>
  <form class="abs booking">
    <div class="booking-head">
      <h2>BOOK YOUR FREIGHT IN 3 MINUTES</h2>
      <p>Lorem Ipsum is simply dummy text of the printing and type-setting industry.</p>
    </div>
    <div class="field" style="top:51px">YOUR NAME</div>
    <div class="field" style="top:78px">EMAIL ADDRESS</div>
    <div class="field" style="top:105px;width:114px">TRANSPORT DATE</div>
    <div class="cal"></div>
    <div class="book-btn">NEXT STEP TO BOOKING</div>
  </form>
  <div class="abs hero-dots"><i></i><i></i><i class="on"></i><i></i><i></i></div>

  <div class="abs sec-head" style="top:298px"><p>Want to get benfits from us,Then check</p><h2>OUR SERVICES</h2></div>

  <div class="abs service" style="left:195px">
    <svg width="30" height="30" viewBox="0 0 30 30"><circle cx="15" cy="15" r="13" fill="#333"/><path d="M4 20l20-9-3 5-13 6z" fill="#8cbf2d"/></svg>
    <h3>Air Freight</h3>
    <p>Lorem Ipsum is simply dummy text of the printing and typesetting indus-try. Lorem Ipsum has been the industry's standard dummy text ever since the 1500s</p>
    <span class="more">READ MORE ▸</span>
  </div>
  <div class="abs service" style="left:326px">
    <svg width="40" height="30" viewBox="0 0 40 30"><circle cx="14" cy="14" r="12" fill="none" stroke="#333" stroke-width="2"/><path d="M2 14h24M14 2v24" stroke="#333" stroke-width="1.2"/><rect x="16" y="16" width="22" height="8" fill="#8cbf2d"/><rect x="20" y="11" width="10" height="5" fill="#8cbf2d"/></svg>
    <h3>Ocean Freight</h3>
    <p>Lorem Ipsum is simply dummy text of the printing and typesetting indus-try. Lorem Ipsum has been the industry's standard dummy text ever since the 1500s</p>
    <span class="more">READ MORE ▸</span>
  </div>
  <div class="abs service" style="left:457px">
    <svg width="40" height="30" viewBox="0 0 40 30"><path d="M3 12L17 3l14 9v16H3z" fill="none" stroke="#333" stroke-width="2"/><rect x="8" y="15" width="5" height="4" fill="#333"/><rect x="14" y="15" width="5" height="4" fill="#333"/><rect x="8" y="20" width="5" height="4" fill="#333"/><rect x="14" y="20" width="5" height="4" fill="#333"/><rect x="24" y="18" width="12" height="8" fill="#8cbf2d"/></svg>
    <h3>Warehousing &amp; Distribution</h3>
    <p>Lorem Ipsum is simply dummy text of the printing and typesetting indus-try. Lorem Ipsum has been the industry's standard dummy text ever since the 1500s</p>
    <span class="more">READ MORE ▸</span>
  </div>

  <section class="abs products"></section>
  <div class="abs sec-head" style="top:492px"><p>Our industry solutions cover these</p><h2>PRODUCTS</h2></div>
  <div class="abs tile" style="left:186px;top:526px"><span>Flowers</span><div role="img" aria-label="Red roses" style="background:linear-gradient(135deg,#c8141c,#7a1010)"></div></div>
  <div class="abs tile" style="left:286px;top:526px"><span class="grey">Fruits&amp;Vegetables</span><div role="img" aria-label="Fresh fruits and vegetables" style="background:linear-gradient(135deg,#d8a020,#6a8a2a)"></div></div>
  <div class="abs tile" style="left:390px;top:526px"><span>Live Animals</span><div role="img" aria-label="Puppy and kitten" style="background:linear-gradient(135deg,#9a7a60,#d8b88a)"></div></div>
  <div class="abs tile" style="left:490px;top:526px"><span class="grey">Automotives</span><div role="img" aria-label="Car engine" style="background:linear-gradient(135deg,#777,#2a2a2a)"></div></div>
  <div class="abs tile" style="left:186px;top:614px"><span class="grey">Consumer Goods</span><div role="img" aria-label="Packaged consumer goods" style="background:linear-gradient(135deg,#3a6ab0,#e0e0e0)"></div></div>
  <div class="abs tile" style="left:286px;top:614px"><span>Industrial Products</span><div role="img" aria-label="Steel gears" style="background:linear-gradient(135deg,#aaa,#444)"></div></div>
  <div class="abs tile" style="left:390px;top:614px"><span class="grey">Oil &amp; Gas</span><div role="img" aria-label="Offshore oil rig" style="background:linear-gradient(#8aa0d0,#1e3a7a)"></div></div>
  <div class="abs tile" style="left:490px;top:614px"><span>Pharma Products</span><div role="img" aria-label="Medicine capsules" style="background:linear-gradient(135deg,#d83030,#f0f0f0)"></div></div>

  <section class="abs testimonial"></section>
  <div class="abs sec-head on-dark" style="top:729px"><p>Share your view about our services here</p><h2>OUR CUSTOMER SAYS</h2></div>
  <div class="abs quote-mark" style="left:190px;top:752px">“</div>
  <p class="abs quote-text">Lorem Ipsum is simply dummy text of the printing and typesetting industry. Lorem Ipsum has been the industry's standard dummy text ever since the 1500s, when an unknown printer took a galley of type and scrambled it to make a type specimen book. It has survived not only five centuries</p>
  <div class="abs quote-mark" style="left:448px;top:784px">”</div>
  <div class="abs author">Delmont,<small>Australia</small></div>
  <div class="abs avatar" role="img" aria-label="Customer portrait"></div>
  <div class="abs dots"><i></i><i></i><i class="on"></i><i></i><i></i></div>

  <div class="abs sec-head" style="top:918px"><p>Easy access of our booking services</p><h2>GET YOUR QUOTE</h2></div>
  <form class="abs quote-panel"></form>
  <div class="abs q-field" style="left:218px;top:970px">FULL NAME</div>
  <div class="abs q-field" style="left:329px;top:970px">EMAIL ADDRESS</div>
  <div class="abs q-field" style="left:440px;top:970px">MOBILE NUMBER</div>
  <div class="abs q-field select" style="left:218px;top:998px">PRODUCT NAME</div>
  <div class="abs q-field select" style="left:329px;top:998px">FREIGHT TYPE</div>
  <div class="abs q-field select" style="left:440px;top:998px">DELIVERY LOCATION</div>
  <div class="abs quote-btn">GET QUOTE NOW</div>

  <footer class="abs footer"></footer>
  <div class="abs foot-brand"><span class="dot"></span>Corvana Freight</div>
  <div class="abs foot-col" style="left:312px;top:1100px;width:105px">
    <h4>CONTACT US</h4>
    <div class="contact-row">
      <svg width="7" height="8" viewBox="0 0 7 8"><path d="M3.5 0a3 3 0 0 1 3 3c0 2-3 5-3 5S.5 5 .5 3a3 3 0 0 1 3-3z" fill="#222"/></svg>
      <p>Lorem Ipsum is simply dummy text of the printing and typesetting industry. Lorem Ipsum has been</p>
    </div>
    <div class="contact-row">
      <svg width="7" height="7" viewBox="0 0 7 7"><path d="M1 1c0 3 2 5 5 5l.5-1.5-1.5-.8-.8.8C3 4 2.5 3.5 2 2.7l.8-.8L2 .5z" fill="#222"/></svg>
      <p>+1-555-014729</p>
    </div>
    <div class="contact-row">
      <svg width="7" height="7" viewBox="0 0 7 7"><circle cx="3.5" cy="3.5" r="3" fill="none" stroke="#222"/></svg>
      <p>www.corvanafreight.example</p>
    </div>
  </div>
  <div class="abs foot-divider"></div>
  <div class="abs foot-col" style="left:435px;top:1100px">
    <h4>QUICK LINKS</h4>
    <ul><li>Home</li><li>About Us</li><li>Services</li><li>Freight Tracking</li><li>Blog</li><li>Contact Us</li></ul>
  </div>
  <div class="abs foot-col" style="left:512px;top:1100px">
    <h4>FOLLOW US ON</h4>
    <div class="social"><span>Chatterpost</span><span>Chirpline</span><span>Vidstream</span><span>Workvine</span><span>Pinboard</span><span>Circleplus</span></div>
  </div>
  <div class="abs bottom">
    <span class="l">All Rights Reserved @ www.corvanafreight.example</span>
    <span class="r">Site map &nbsp;|&nbsp; Terms &amp; Conditions</span>
  </div>

</div>
</body>
</html>
```